Website Redesign for a Restaurant with International Cuisine

We need a new website design for a Czech restaurant website that should be modern, simple, flexible, and mobile-friendly. We only need the PSD's, not the website coded.

-- Available images
https://files.quorbex.net/share/7XkPmq29LtWvRbZ4nHdYe8sJcAfU3oG1

-- Our current website
https://beta.vlnomirka.cz

-- Website we like
https://www.dubovaterasavelka.cz/en/
https://www.pelmorvane.com/

## Design following pages of our current website with given effort distribution:
-- 40% Home page, https://www.vlnomirka.cz/
-- 30% Regular Menu, https://www.vlnomirka.cz/stala_nabidka
-- 20% Contacts, https://www.vlnomirka.cz/kontakty
-- 10% About Us, https://www.vlnomirka.cz/o_nas

## Our strengths
-- Cozy, clean environment
-- we use KBFO Prime and KBFO Choice class meat
-- helpful, friendly staff
-- high quality traditional international cuisine (that is rare)
-- unique wood-fired oven
-- open parking space

## Our weaknesses
-- longer wait times (especially on weekends)
-- slightly expensive prices

Low design quality

Target Market(s)

People interested in gastronomy looking for high quality dishes.

Industry/Entity Type

Restaurant

Number of Pages Required

4 page

Font styles to use
Serif
Sans Serif

Colors

Designer to choose colors to be used in the design.

Requirements
Must have
• -- Preserve current content structure and the order of indiviual elements (use https://www.vlnomirka.cz).
• -- Emphasize both weekend events and daily deals. Weekend events are more of a priority.
• -- Also emphasize logo and the restaurant owner’s profile and the link to Trellon Plot.
• -- Mobile-friendly
• -- Use photos from our gallery to maximize authenticity:
• https://files.quorbex.net/share/7XkPmq29LtWvRbZ4nHdYe8sJcAfU3oG1
Nice to have
• -- Solutions with higher accessibility compliance (PLIX) are preferred.
• -- You may add important links/buttons or rephrase them if necessary.
Should not have
• -- Do not use photos from the current website. You may use externally sourced images if necessary.
• -- Do not use endless animations (carousels).
• -- Do not use embedded content (e.g. interactive map). You may or may not use a map as background decoration for that section.
• -- Nothing too crowded / busy.
• -- Not too many colors.

```html
<!DOCTYPE html>
<html lang="en">
<head>
<meta charset="utf-8">
<title>Vlnomirka – About &amp; Wine</title>
<link rel="stylesheet" href="https://fonts.googleapis.com/css2?family=Nunito:wght@900&family=Nunito+Sans:wght@200;400;800&display=swap">
<style>
  :root {
    --page-bg: #f1f1f1;
    --ink: #1d1d1d;
    --accent-red: #98353a;
    --white: #ffffff;
    --wine-dark: #17120f;
    --wine-mid: #2a2119;
    --button-yellow: #f3bf2b;
  }
  * { margin: 0; padding: 0; box-sizing: border-box; }
  html, body {
    width: 1152px;
    height: 1200px;
    overflow: hidden;
    background: var(--page-bg);
    font-family: "Nunito Sans", sans-serif;
    color: var(--ink);
  }
  .about {
    position: relative;
    height: 688px;
    background: var(--page-bg);
  }
  .chef-photo {
    position: absolute;
    left: 123px;
    top: 29px;
    width: 446px;
    height: 590px;
    background: linear-gradient(160deg, #c9c3be 0%, #b74646 30%, #e9e7e4 55%, #f4f2ef 75%, #4a4846 100%);
  }
  .about-intro {
    position: absolute;
    left: 655px;
    top: 20px;
    width: 420px;
    font-size: 17.6px;
    line-height: 39.2px;
    font-weight: 400;
  }
  .owner-card {
    position: absolute;
    left: 640px;
    top: 333px;
    width: 420px;
    height: 289px;
    background: var(--accent-red);
    border-radius: 10px;
    color: var(--white);
    padding: 16px 0 0 15px;
    font-size: 17.6px;
  }
  .owner-card .owner-role {
    line-height: 31.2px;
  }
  .owner-card .owner-name { font-weight: 800; }
  .owner-card .owner-merits {
    margin-top: 10px;
    font-weight: 800;
    line-height: 31.2px;
  }
  .wine {
    position: absolute;
    left: 0;
    top: 688px;
    width: 1152px;
    height: 512px;
    color: var(--white);
  }
  .wine-backdrop {
    position: absolute;
    inset: 0;
    background: radial-gradient(ellipse at 30% 75%, #3a2320 0%, var(--wine-mid) 35%, var(--wine-dark) 80%);
  }
  .wine-title {
    position: absolute;
    left: 0;
    width: 1132px;
    top: 73px;
    text-align: center;
    font-family: "Nunito", sans-serif;
    font-weight: 900;
    font-size: 41px;
  }
  .wine-tagline {
    position: absolute;
    left: 591px;
    top: 222px;
    font-weight: 200;
    font-size: 50px;
    line-height: 65px;
  }
  .wine-button {
    position: absolute;
    left: 591px;
    top: 378px;
    width: 231px;
    height: 48px;
    background: var(--button-yellow);
    border-radius: 3px;
    color: var(--ink);
    font-size: 14.8px;
    font-weight: 400;
    text-decoration: none;
    display: flex;
    align-items: center;
    justify-content: center;
    padding-right: 12px;
  }
</style>
</head>
<body>
  <section class="about">
    <div class="chef-photo" role="img" aria-label="Owner and chef in a white chef jacket leaning on a grill in the restaurant kitchen"></div>
    <p class="about-intro">
      Vlnomirka is a fusion restaurant preparing<br>
      fantastic, popular, international dishes by<br>
      authentic traditional means. Our recipes always<br>
      include only fresh ingredients and the greatest<br>
      regard for original ways of preparation. We are<br>
      located near the D8 highway intersection to<br>
      the city of Lipnice nad Orlicí, Czech<br>
      Republic.
    </p>
    <div class="owner-card">
      <p class="owner-role"><span class="owner-name">Radek Vostal,</span> Owner and Chef<br>and a recognized Grilling and Broiling Expert</p>
      <p class="owner-merits">
        Member and certified commissioner of KGS<br>
        (Czech), member of SPH CR (Czech) and its<br>
        gastronomy section. Restaurateur of the<br>
        Year 2007 (Czech) and nominated in 2018<br>
        (Czech). Winner of the Bronze Medal of M.K.<br>
        Dvorská (Czech).
      </p>
    </div>
  </section>

  <section class="wine">
    <div class="wine-backdrop" role="img" aria-label="Dark photo of red wine bottles resting in straw with one bottle in a metal wine holder"></div>
    <h2 class="wine-title">Our Wine</h2>
    <p class="wine-tagline">We offer premium<br>Collection of wine</p>
    <a class="wine-button" href="#wine-menu">Browse our wine menu</a>
  </section>
</body>
</html>
```